Licensed Fabrication Operator Training Program

We need a flyer to advertise a training program to business. I will attach a rough draft "original file" that we need enhanced to look professional. Details to the program are here https://www.vornelskills.org/credentials/fabrication-credential-lfo/ We want it to look clean and professional.

Please use the information that is on the "original file" rough draft. I have attached an example pdf, the reason I don't like the example is because it has too many words and looks out of date.

Font styles to use
Serif
Sans Serif

```html
<!DOCTYPE html>
<html lang="en">
<head>
<meta charset="utf-8">
<title>Licensed Fabrication Operator Program</title>
<link href="https://fonts.googleapis.com/css2?family=Oswald:wght@400;500&family=Montserrat:wght@400;500&display=swap" rel="stylesheet">
<style>
  :root {
    --navy: #131933;
    --panel: #16283c;
    --teal: #1a9e91;
    --white: #ffffff;
    --grey: #b9bec8;
  }
  html, body { margin: 0; padding: 0; overflow: hidden; background: var(--navy); }
  .flyer {
    position: relative; width: 848px; height: 1200px; overflow: hidden;
    background: var(--navy); color: var(--white);
    font-family: "Montserrat", sans-serif;
  }
  .abs { position: absolute; }

  .seal { left: 42px; top: 47px; width: 145px; height: 110px; }

  .title {
    right: 28px; top: 126px; margin: 0; text-align: right;
    font-family: "Oswald", sans-serif; font-weight: 500;
    font-size: 41px; line-height: 55px; letter-spacing: 5px;
  }

  .pillar {
    top: 253px; width: 89px; height: 55px; background: var(--teal);
    display: flex; align-items: center; justify-content: center; text-align: center;
    font-family: "Oswald", sans-serif; font-size: 13px; letter-spacing: 1.6px; line-height: 16px;
  }
  .pillar.small { font-size: 11px; }

  .quote {
    left: 17px; top: 389px; width: 446px; height: 110px; background: var(--teal);
    box-sizing: border-box; padding: 12px 12px 0 11px; margin: 0;
    font-family: "Oswald", sans-serif; font-size: 8.6px; letter-spacing: 1.3px; line-height: 15px;
  }
  .quote p { margin: 0; }
  .quote .by { margin-top: 12px; padding-left: 12px; line-height: 10px; }

  .feature {
    right: 48px; font-family: "Oswald", sans-serif; font-size: 14px; letter-spacing: 3.6px;
    white-space: nowrap;
  }
  .feature.mid { right: 72px; }

  .shot { top: 515px; height: 117px; }

  .price {
    left: 560px; top: 518px; width: 237px; height: 110px; background: var(--teal);
    display: flex; flex-direction: column; justify-content: center; align-items: center;
    font-family: "Oswald", sans-serif; font-size: 12.5px; letter-spacing: 2.5px; line-height: 23px;
  }

  .skills {
    left: 17px; top: 651px; width: 362px; height: 339px; background: var(--teal);
    box-sizing: border-box; padding: 14px 0 0 9px; overflow: hidden;
  }
  .skills h2 {
    margin: 0 0 0 15px; font-family: "Oswald", sans-serif; font-weight: 400;
    font-size: 31px; letter-spacing: 2px; line-height: 40px;
  }
  .skills ul { list-style: none; margin: 0; padding: 0; }
  .skills li {
    font-size: 14.5px; letter-spacing: 1.2px; line-height: 27.2px; white-space: nowrap;
  }

  .team-photo { left: 384px; top: 651px; width: 257px; height: 339px; }

  .contact {
    left: 651px; top: 651px; width: 182px; height: 339px; background: var(--panel);
    text-align: center; overflow: hidden;
  }
  .contact .mark { margin: 38px auto 0; width: 44px; height: 44px; border-radius: 50%; background: var(--teal); }
  .contact .brand { margin-top: 28px; font-size: 19px; letter-spacing: 2px; line-height: 23px; color: var(--teal); }
  .contact .brand.second { margin-top: 0; color: var(--white); }
  .contact hr { border: 0; border-top: 1px solid var(--white); margin: 10px 0 18px; }
  .contact p { margin: 0; font-size: 12px; letter-spacing: 1.8px; line-height: 21.5px; white-space: nowrap; }
  .contact p.email { font-size: 10.5px; letter-spacing: 0.8px; }
  .contact .onsite { margin-top: 22px; }

  .members-head {
    left: 0; width: 848px; top: 1006px; text-align: center;
    font-size: 19.5px; letter-spacing: 1.9px; white-space: nowrap;
  }

  .members {
    left: 17px; top: 1050px; width: 816px; height: 137px; background: var(--teal);
    box-sizing: border-box; padding: 5px; display: flex; gap: 6px;
  }
  .members .cell {
    flex: 1; background: var(--white); color: var(--navy);
    display: flex; align-items: center; justify-content: center; text-align: center;
    font-family: "Montserrat", sans-serif; font-weight: 500; font-size: 15px; letter-spacing: 1px;
  }
</style>
</head>
<body>
<main class="flyer">
  <svg class="abs seal" viewBox="0 0 145 110" role="img" aria-label="Program certification seal">
    <circle cx="72" cy="55" r="52" fill="#8d939e"/>
  </svg>

  <h1 class="abs title">LICENSED FABRICATION<br>OPERATOR PROGRAM</h1>

  <div class="abs pillar" style="left:407px">SAFETY</div>
  <div class="abs pillar" style="left:510px">QUALITY</div>
  <div class="abs pillar" style="left:613px">PROCESSES</div>
  <div class="abs pillar small" style="left:715px">MAINTENANCE<br>AWARENESS</div>

  <blockquote class="abs quote">
    <p>WE FEEL THAT VORNEL LFO CERTIFICATION COMPLIMENTS NOT ONLY THE QUALIFICATIONS OF THE CANDIDATES WE SEE, BUT ALSO ENHANCES THE KNOWLEDGE, SKILLS, AND ABILITIES OF EXISTING TEAM MEMBERS IN OUR PURSUIT OF MANUFACTURING EXCELLENCE.</p>
    <p class="by">DALE HENSLEY<br>VICE PRESIDENT &amp; GENERAL MANAGER<br>KESTREL DRIVE SYSTEMS</p>
  </blockquote>

  <div class="abs feature" style="top:390px">- ADVANCED MANUFACTURING</div>
  <div class="abs feature mid" style="top:431px">- HANDS ON LEARNING</div>
  <div class="abs feature" style="top:471px">- COLLEGE CREDITS ELIGIBLE</div>

  <svg class="abs shot" style="left:17px;width:125px" role="img" aria-label="Pneumatics training station with blue control unit"><rect width="100%" height="100%" fill="#dde3ea"/></svg>
  <svg class="abs shot" style="left:146px;width:153px" role="img" aria-label="Training panel with blue motor and yellow cabling"><rect width="100%" height="100%" fill="#d6dadf"/></svg>
  <svg class="abs shot" style="left:304px;width:158px" role="img" aria-label="Training software screen with circuit diagram"><rect width="100%" height="100%" fill="#eef0f2"/></svg>

  <div class="abs price">
    <span>120 HOURS</span>
    <span>$2500 PER STUDENT</span>
    <span>WTP REIMBURSEMENT</span>
  </div>

  <section class="abs skills">
    <h2>SKILLS TAUGHT</h2>
    <ul>
      <li>- COMMUNICATION</li>
      <li>- LEAN PRINCIPLES</li>
      <li>- PROBLEM SOLVING</li>
      <li>- TEAMWORK</li>
      <li>- LOCATING INFORMATION</li>
      <li>- SUPPLY CHAIN AND LOGISTICS</li>
      <li>- DATA ANALYSIS</li>
      <li>- TOTAL PRODUCTION MAINTENANCE</li>
      <li>- CUSTOMER SERVICE</li>
      <li>- PROJECT MANAGEMENT</li>
    </ul>
  </section>

  <svg class="abs team-photo" role="img" aria-label="Trainees gathered around a hands-on training station">
    <defs><linearGradient id="room" x1="0" y1="0" x2="0" y2="1"><stop offset="0" stop-color="#7d7a6e"/><stop offset="1" stop-color="#3a3d4a"/></linearGradient></defs>
    <rect width="100%" height="100%" fill="url(#room)"/>
  </svg>

  <aside class="abs contact">
    <div class="mark"></div>
    <div class="brand">MARLOWE</div>
    <div class="brand second">CONSULTING</div>
    <hr>
    <p>CALL TO SCHEDULE</p>
    <p>555 014 2290</p>
    <p class="email">owen@marlowelean.com</p>
    <p class="onsite">ON-SITE</p>
    <p>TRAINING AVAILABLE</p>
  </aside>

  <div class="abs members-head">VORNEL CERTIFICATION SCHEME COMMITTEE MEMBERS WORK AT:</div>

  <div class="abs members">
    <div class="cell">VORNEL</div>
    <div class="cell">CALDERA</div>
    <div class="cell">NORTHGATE</div>
    <div class="cell">RIDGEWAY MOTORS</div>
    <div class="cell">STANDARDS UNION</div>
    <div class="cell">HOLLOWAY</div>
  </div>
</main>
</body>
</html>
```